Steady Harbor- A Patient's Complete Guide to Handling a Serious Diagnosis

This is a book cover sall the aspects of managing a cancer diagnosis from what to do when you first get the diagnosis to magaing finances and lift after cancer.

Successful candidate will familarize themselves with the elements of the book and incorporate the elements into the main graphic which is a fist punching down from above crushing the word cancer.

I have "Steady" Harbor, it shoudl be Crushing.

Also, the word crushing may be above then the fist coming down on the word cancer.

```html
<!DOCTYPE html>
<html lang="en">
<head>
<meta charset="utf-8">
<title>Steady Harbor – Book Cover</title>
<link rel="stylesheet" href="https://fonts.googleapis.com/css2?family=Anton&family=Roboto+Condensed:wght@400;500&family=Source+Sans+3:wght@400&display=swap">
<style>
  :root {
    --night: #0c0a3e;
    --night-deep: #07062a;
    --paper: #ffffff;
    --alarm-red: #e50b0b;
    --skin-dark: #7a4a30;
    --skin-mid: #c99478;
    --skin-light: #e6c2a8;
  }
  * { margin: 0; padding: 0; box-sizing: border-box; }
  html, body { width: 1200px; height: 871px; overflow: hidden; background: var(--night-deep); }
  .cover {
    position: relative;
    width: 1200px; height: 871px;
    overflow: hidden;
    background: var(--night);
  }
  .cell-field {
    position: absolute; inset: 0;
    background:
      radial-gradient(ellipse 260px 200px at 780px 280px, rgba(90,40,120,.45), transparent 70%),
      radial-gradient(ellipse 300px 220px at 1080px 520px, rgba(40,60,150,.45), transparent 70%),
      radial-gradient(ellipse 260px 180px at 650px 650px, rgba(40,55,140,.4), transparent 70%),
      radial-gradient(ellipse 220px 160px at 900px 120px, rgba(70,35,110,.35), transparent 70%),
      linear-gradient(90deg, var(--night-deep) 0%, var(--night) 40%, #13176a 100%);
  }
  .back-copy {
    position: absolute;
    left: 71px; top: 131px;
    width: 439px;
    font-family: "Source Sans 3", sans-serif;
    font-size: 16.6px;
    line-height: 24.2px;
    color: var(--paper);
    text-align: justify;
  }
  .back-copy p + p { margin-top: 24.2px; }

  .spine {
    position: absolute;
    left: 578px; top: 0;
    width: 44px; height: 871px;
  }
  .spine-title, .spine-author {
    position: absolute;
    left: 50%;
    white-space: nowrap;
  }
  .spine-title {
    top: 378px;
    transform: translate(-50%, -50%) rotate(90deg);
    font-family: "Anton", sans-serif;
    font-size: 33px;
    letter-spacing: .5px;
  }
  .spine-title .word-one { color: var(--paper); }
  .spine-title .word-two { color: var(--alarm-red); margin-left: 12px; }
  .spine-author {
    top: 727px;
    transform: translate(-50%, -50%) rotate(90deg);
    font-family: "Roboto Condensed", sans-serif;
    font-weight: 500;
    font-size: 17px;
    color: var(--paper);
  }

  .fist { position: absolute; }
  .fist-top {
    left: 841px; top: 0; width: 133px; height: 232px;
    background: linear-gradient(180deg, var(--skin-dark), #5a3322);
    border-radius: 0 0 40px 40px;
  }
  .fist-left {
    left: 614px; top: 282px; width: 143px; height: 142px;
    background: linear-gradient(90deg, rgba(230,194,168,0) 0%, var(--skin-light) 30%, var(--skin-mid) 100%);
    border-radius: 0 60px 60px 0;
  }
  .fist-right {
    left: 1042px; top: 286px; width: 158px; height: 143px;
    background: linear-gradient(270deg, var(--skin-mid), var(--skin-light));
    border-radius: 60px 0 0 60px;
  }

  .title {
    position: absolute;
    left: 728px; top: 196px;
    width: 375px;
    font-family: "Anton", sans-serif;
    text-align: center;
    line-height: 1;
  }
  .title .word-one, .title .word-two {
    display: block;
    font-size: 122px;
    letter-spacing: 1px;
    transform: scaleX(.95);
  }
  .title .word-one { color: var(--paper); }
  .title .word-two { color: var(--alarm-red); margin-top: 4px; }

  .subtitle {
    position: absolute;
    left: 690px; top: 540px;
    width: 430px;
    font-family: "Roboto Condensed", sans-serif;
    font-weight: 500;
    font-size: 33px;
    line-height: 46px;
    color: var(--paper);
    text-align: center;
  }
  .author {
    position: absolute;
    left: 690px; top: 776px;
    width: 430px;
    font-family: "Roboto Condensed", sans-serif;
    font-weight: 500;
    font-size: 40px;
    color: var(--paper);
    text-align: center;
    letter-spacing: .5px;
  }
</style>
</head>
<body>
<main class="cover">
  <div class="cell-field" role="img" aria-label="Microscope photograph of blue and red stained cells with faint molecule diagrams"></div>

  <section class="back-copy">
    <p>Lorem ipsum dolor sit amet, consectetur adipiscing elit. Pellentesque elementum purus pulvinar euismod hendrerit. Mauris ac risus tristique, condimentum massa in, hendrerit nulla. Quisque pulvinar sagittis leo, in ultrices massa hendrerit eget. Quisque ac imperdiet nulla. Etiam tortor felis, tincidunt ac auctor et, euismod sed arcu. Mauris risus mauris, consectetur sed nisi et, commodo tincidunt urna. Pellentesque porta, dui quis mollis sollicitudin, justo est consequat augue, sit amet elementum nisl quam maximus massa. Vestibulum tincidunt mauris interdum ipsum egestas lobortis.</p>
    <p>Maecenas ut nisl nec tortor pretium ultricies. Vestibulum blandit, erat eu ornare lobortis, est orci dictum augue, at commodo purus augue rhoncus augue. Suspendisse egestas felis lorem, ut vestibulum est porttitor et. Nam tempus, dolor vel placerat auctor, ex tellus laoreet lorem, non vestibulum elit nisl quis nisl.</p>
    <p>Maecenas suscipit quis quam non auctor. Aenean sed fermentum orci. Etiam sit amet lorem velit. Etiam feugiat sapien a fermentum semper. Etiam maximus condimentum lectus sed sodales. Nunc auctor erat non erat consectetur commodo. Sed in semper nulla. In tincidunt, diam sed gravida facilisis, neque mauris cursus ante, eget finibus elit purus in dolor.</p>
  </section>

  <section class="spine">
    <div class="spine-title"><span class="word-one">STEADY</span><span class="word-two">HARBOR</span></div>
    <div class="spine-author">DANA M. WHITLOCK, MD</div>
  </section>

  <div class="fist fist-top" role="img" aria-label="Photograph of a clenched fist reaching down from above"></div>
  <div class="fist fist-left" role="img" aria-label="Photograph of a clenched fist reaching in from the left"></div>
  <div class="fist fist-right" role="img" aria-label="Photograph of a clenched fist reaching in from the right"></div>

  <h1 class="title">
    <span class="word-one">STEADY</span>
    <span class="word-two">HARBOR</span>
  </h1>

  <p class="subtitle">A Patient's Complete Guide<br>to Handling a Serious Diagnosis</p>

  <p class="author">DANA M. WHITLOCK, MD</p>
</main>
</body>
</html>
```